Security Warning Sign

We have an existing sign that needs an update. I have attached a picture of the current square sign. We need to maintain the same wording. It needs to be professional and appropriate to attach to our customers fence. Also attached is a copy of our building sign which may lend some inspiration and hopefully the ai format will assist. The final sign will be 600mm x 600mmOur website is www.halvorngate.com.au

```html
<!DOCTYPE html>
<html lang="en">
<head>
<meta charset="utf-8">
<title>Halvorngate Security Services – Surveillance Warning Sign</title>
<link href="https://fonts.googleapis.com/css2?family=Open+Sans:wght@800&family=Roboto:wght@400;900&display=swap" rel="stylesheet">
<style>
  :root {
    --bg-light: #2b2b2b;
    --bg-dark: #1d1d1d;
    --orange: #f38522;
    --white: #ffffff;
    --stripe-grey: #4a4a4a;
  }
  html, body {
    margin: 0;
    padding: 0;
    width: 1200px;
    height: 1199px;
    overflow: hidden;
    background: var(--bg-dark);
  }
  .sign {
    display: block;
    width: 1200px;
    height: 1199px;
  }
  .headline {
    font-family: "Roboto", Arial, sans-serif;
    font-weight: 900;
    fill: var(--orange);
  }
  .notice {
    font-family: "Roboto", Arial, sans-serif;
    font-weight: 400;
    fill: var(--white);
  }
  .brand-name,
  .phone-number,
  .website {
    font-family: "Open Sans", Arial, sans-serif;
    font-weight: 800;
    fill: var(--white);
  }
  .camera-icon { fill: var(--white); }
  .brand-mark { fill: var(--orange); }
  .phone-band { fill: var(--orange); }
  .band-stripe { fill: var(--stripe-grey); }
  .phone-icon { fill: var(--white); }
</style>
</head>
<body>
<svg class="sign" viewBox="0 0 1200 1199" xmlns="http://www.w3.org/2000/svg">
  <defs>
    <linearGradient id="backdrop" x1="0" y1="0" x2="1" y2="1">
      <stop offset="0" stop-color="var(--bg-light)"/>
      <stop offset="0.5" stop-color="#252525"/>
      <stop offset="1" stop-color="var(--bg-dark)"/>
    </linearGradient>
  </defs>

  <rect class="backdrop" width="1200" height="1199" fill="url(#backdrop)" role="img" aria-label="Dark faceted geometric background texture"/>

  <text class="headline" x="597" y="233" font-size="222" text-anchor="middle" textLength="969" lengthAdjust="spacingAndGlyphs">WARNING</text>

  <rect class="camera-icon" x="49" y="275" width="233" height="149" rx="18" role="img" aria-label="Security camera icon facing right"/>
  <rect class="camera-icon" x="917" y="275" width="234" height="149" rx="18" role="img" aria-label="Security camera icon facing left"/>

  <g class="notice" font-size="94" text-anchor="middle">
    <text x="600" y="407" textLength="544" lengthAdjust="spacingAndGlyphs">ELECTRONIC</text>
    <text x="600" y="518" textLength="664" lengthAdjust="spacingAndGlyphs">SURVEILLANCE</text>
    <text x="598" y="630" textLength="725" lengthAdjust="spacingAndGlyphs">AND RECORDING</text>
    <text x="599" y="740" textLength="874" lengthAdjust="spacingAndGlyphs">DEVICES INSTALLED</text>
    <text x="601" y="852" textLength="588" lengthAdjust="spacingAndGlyphs">IN THIS AREA</text>
  </g>

  <circle class="brand-mark" cx="191" cy="1015" r="60"/>
  <g class="brand-name" font-size="46">
    <text x="295" y="987" textLength="290" lengthAdjust="spacingAndGlyphs">HALVORNGATE</text>
    <text x="295" y="1033">SECURITY</text>
    <text x="295" y="1077">SERVICES</text>
  </g>

  <polygon class="band-stripe" points="648,976 660,976 638,1062 626,1062"/>
  <polygon class="phone-band" points="668,976 705,976 685,1062 648,1062" />
  <polygon class="phone-band" points="712,976 1094,976 1094,1062 663,1062"/>
  <path class="phone-icon" d="M720 1000c3-4 8-5 11-2l7 8c2 3 2 6-1 8l-4 3c2 6 7 12 13 15l3-4c2-3 6-3 8-1l8 7c3 3 2 8-2 10l-5 4c-5 3-12 2-19-3-9-6-17-15-22-25-3-7-3-13 1-17z"/>
  <text class="phone-number" x="768" y="1036" font-size="48" textLength="286" lengthAdjust="spacingAndGlyphs">1300 555 014</text>

  <text class="website" x="600" y="1147" font-size="35" text-anchor="middle">WWW.HALVORNGATE.COM.AU</text>
</svg>
</body>
</html>
```